RP-Steuerberatung WordPress Site fully implemented (tax advisor)

Hello!
I need a little Wordpress Site for my newly founded Tax-Advisor Company.
I am a one-man Office advising in the area of Crypto-Currency.
PLEASE only provide a Design, if you can also Implement a WP-Site afterwards on an existing Webspace.

Please find the Content and Website-Description in the attached Document

Language for the Website is German (for now)

Target Market(s)

Tax-Advisory (specialized in Crypto Currency)

Coding

Coded - Design and coding required

Number of Pages Required

5+ page

Font styles to use
Sans Serif

Requirements
Must have
• Wordpress Implementation afterwards - Details according to attached Project Information Document

```html
<!DOCTYPE html>
<html lang="de">
<head>
<meta charset="utf-8">
<title>RP-Steuerberatung – Seitenübersicht</title>
<link href="https://fonts.googleapis.com/css2?family=Poppins:wght@300;400;500;600;700;800&display=swap" rel="stylesheet">
<style>
:root{
  --board:#a9adb7;
  --navy:#13213f;
  --navy-deep:#0e1a35;
  --topbar:#1a2949;
  --text:#6b7280;
  --muted:#9aa1ad;
  --white:#ffffff;
  --soft:#f4f5f7;
  --line:#e3e5e9;
  --badge:#a3a7ae;
}
*{box-sizing:border-box;margin:0;padding:0}
html,body{width:1200px;height:2312px;overflow:hidden}
body{background:var(--board);font-family:'Poppins',sans-serif;color:var(--text);position:relative}
.board-title{position:absolute;width:484px;text-align:center;color:var(--white);font-weight:700;font-size:15px;letter-spacing:.3px}
.page{position:absolute;width:484px;background:var(--white);box-shadow:0 14px 34px rgba(20,30,60,.35);overflow:hidden}

/* top bar */
.topbar{height:18px;background:var(--topbar);display:flex;align-items:center;padding:0 32px 0 37px;color:var(--white);font-size:5.5px}
.social{display:flex;gap:7px;align-items:center}
.social i{width:5px;height:5px;background:var(--white);border-radius:1px;display:block}
.topbar .contact{margin-left:auto;display:flex;gap:28px}
.topbar b{font-weight:600}

/* nav */
.nav{height:30px;display:flex;align-items:center;padding:0 38px 0 44px;border-bottom:1px solid var(--line)}
.brand{display:flex;align-items:center;gap:5px;color:var(--navy);font-weight:700;font-size:7.2px;letter-spacing:.2px}
.brand .mark{width:11px;height:11px;background:var(--navy);border-radius:2px}
.menu{margin-left:auto;display:flex;align-items:center;gap:13px;font-size:5.8px;color:var(--text);font-weight:500}
.menu .on{color:var(--navy);font-weight:700}
.menu .btn-k{border:1.3px solid var(--navy);border-radius:10px;padding:3px 10px;color:var(--navy);font-weight:700}

/* hero */
.hero{height:218px;position:relative;overflow:hidden}
.hero .photo{position:absolute;inset:0;background:linear-gradient(90deg,#f7f8fa 0%,#eef1f5 40%,#9fb0c9 62%,#3a4e74 80%,#1e2e4d 100%)}
.hero .copy{position:absolute;left:38px;top:52px;width:230px}
.hero .copy.low{top:70px}
.hero h1{font-size:16px;line-height:21px;font-weight:600;color:var(--badge)}
.hero h1 strong{display:block;color:var(--navy);font-weight:800;font-size:17px}
.hero p{font-size:6.6px;line-height:12px;color:var(--navy);margin:8px 0 12px}
.pill{display:inline-flex;align-items:center;gap:6px;background:var(--navy);color:var(--white);font-weight:700;font-size:5.5px;border-radius:10px;padding:6px 10px}
.pill svg{width:7px;height:7px}
.arrow-nav{position:absolute;top:88px;width:14px;height:26px;background:rgba(255,255,255,.55);display:flex;align-items:center;justify-content:center;color:#fff;font-size:8px}

/* features */
.features{height:112px;display:flex;padding:22px 38px 0}
.feature{flex:1;padding:0 12px 0 0;border-right:1px solid var(--line);margin-right:12px}
.feature:last-child{border:0;margin:0}
.num{display:inline-block;background:var(--badge);color:var(--white);font-weight:700;font-size:10px;padding:4px 5px;border-radius:2px;margin-bottom:10px}
.feature p{font-size:6.2px;line-height:12.5px}

/* banner */
.banner{height:113px;position:relative;display:flex;align-items:center;justify-content:center}
.banner .photo{position:absolute;inset:0;background:linear-gradient(110deg,#1b2a49 0%,#5a4234 35%,#2c3b5a 60%,#14213e 100%)}
.banner h2{position:relative;color:var(--white);font-weight:700;font-size:15px;letter-spacing:.4px}

/* footer */
.footer{height:158px;background:var(--navy-deep);display:grid;grid-template-columns:197px 108px 1fr;padding:35px 37px 0;color:var(--muted);font-size:6.2px;line-height:12.5px}
.footer .brand{color:var(--white);margin-bottom:5px}
.footer .brand .mark{background:var(--white)}
.footer h4{color:var(--white);font-size:7px;font-weight:700;margin-bottom:4px}
.footer .copy{margin-top:12px;font-size:5.5px}
.footer ul{list-style:none;line-height:15.2px}
.footer li::before{content:"› ";color:var(--white)}
.ci{display:flex;gap:8px;align-items:center;margin-bottom:6px;line-height:9px}
.ci .ico{width:16px;height:16px;background:var(--badge);border-radius:2px}
.ci span{color:var(--white)}
.ci small{display:block;color:var(--muted);font-size:5.8px}
.social-row{display:flex;gap:12px;align-items:center}
.social-row i{width:4px;height:4px;background:var(--white);display:block;border-radius:1px}

/* service */
.section{padding:0 38px;position:relative}
.lead{font-size:6.3px;line-height:12.5px;text-align:center;padding:30px 20px 0}
.checks{list-style:none;position:absolute;left:38px;top:92px;width:208px}
.checks li{display:flex;gap:8px;font-size:6.3px;line-height:12.5px;margin-bottom:12px}
.checks svg{flex:none;width:7px;height:7px;margin-top:3px}
.framed{position:absolute;border:2px solid #c9ccd2;border-radius:8px}
.framed .photo{position:absolute;border-radius:8px}
.center{text-align:center}

/* colleagues */
.q{font-size:7.8px;line-height:13px;font-weight:700;color:var(--text);text-align:center;padding:30px 50px 8px}

/* about */
.intro{height:265px;position:relative}
.ring{position:absolute;left:38px;top:35px;width:158px;height:158px;border-radius:50%;border:1px dashed var(--navy)}
.ring .photo{position:absolute;inset:10px;border-radius:50%;background:radial-gradient(circle at 50% 45%,#d9dadd 0%,#b9bcc2 60%,#8d929b 100%);border:5px solid #eceef1}
.namecard{position:absolute;left:64px;top:203px;width:100px;background:var(--navy);color:var(--white);text-align:center;padding:5px 0;border-radius:2px}
.namecard b{display:block;font-size:7.5px;font-weight:600}
.namecard small{font-size:5px}
.about-text{position:absolute;left:225px;top:33px;width:222px;font-size:6.2px;line-height:12.8px}
.about-text p{margin-bottom:9px}
.timeline{height:307px;background:var(--soft);padding:35px 37px 0;position:relative}
.tl-cols{display:grid;grid-template-columns:1fr 1fr;gap:27px}
.tl-cols h5{font-size:7.5px;font-weight:600;color:var(--navy);margin-bottom:12px}
.row{display:flex;gap:13px;padding:0 0 14px;margin-bottom:13px;border-bottom:1px solid #d6d9de;font-size:6.2px;line-height:12.5px}
.row:last-child{border:0}
.yr{flex:none;background:var(--navy);color:var(--white);font-weight:700;font-size:6px;padding:3px 8px;border-radius:2px;height:16px}
.yr.g{background:var(--badge)}
.tl-btn{position:absolute;left:0;right:0;bottom:36px;text-align:center}
</style>
</head>
<body>

<!-- column titles -->
<div class="board-title" style="left:82px;top:72px">HOME PAGE OPTION 1</div>
<div class="board-title" style="left:634px;top:72px">SERVICE PAGE</div>
<div class="board-title" style="left:82px;top:689px">HOME PAGE OPTION 2</div>
<div class="board-title" style="left:634px;top:944px">SERVICES FOR COLLEAGUES PAGE</div>
<div class="board-title" style="left:82px;top:1306px">ABOUT ME PAGE</div>

<!-- HOME 1 -->
<section class="page" style="left:82px;top:110px;height:536px">
  <div class="topbar"><div class="social"><i></i><i></i><i></i></div><div class="contact"><span>Email: office@rp-steuer.example</span><span>Phone: <b>+43 512 000 471</b></span></div></div>
  <nav class="nav"><div class="brand"><span class="mark"></span>RP STEUERBERATUNG</div><div class="menu"><span class="on">HOME</span><span>LEISTUNGEN ▾</span><span>ÜBER MICH</span><span>IMPRESSUM</span><span class="btn-k">KONTAKT ›</span></div></nav>
  <div class="hero">
    <div class="photo" role="img" aria-label="Foto: zwei Berater im Anzug am Schreibtisch mit Krypto-Münzen im Vordergrund"></div>
    <div class="copy"><h1>WILLKOMMEN BEI<strong>RP-STEUERBERATUNG!</strong></h1><p>Ihrem Spezialisten bei allen steuerlichen Themen rund um Einkünfte &amp; Vermögen aus Krypto-Assets.</p><span class="pill">WEITER ZU UNSEREN LEISTUNGEN <svg viewBox="0 0 10 10"><circle cx="5" cy="5" r="4" fill="none" stroke="#fff"/><path d="M4 3l2 2-2 2" fill="none" stroke="#fff"/></svg></span></div>
  </div>
  <div class="features">
    <div class="feature"><span class="num">01</span><p>Dann mach ich eine Schweizer Holding Gesellschaft- dort zahlt man fast keine Steuern</p></div>
    <div class="feature"><span class="num">02</span><p>Dann melde ich einfach meinen Hauptwohnsitz in Österreich ab</p></div>
    <div class="feature"><span class="num">03</span><p>Dann lass ich meine Kryptos auf einer Börse in Singapur, dort ist das steuerfrei</p></div>
  </div>
  <footer class="footer">
    <div><div class="brand"><span class="mark"></span>RP STEUERBERATUNG</div>Ihrem Spezialisten bei allen steuerlichen Themen rund um Einkünfte &amp; Vermögen aus Krypto-Assets.<div class="copy">Copyright © 2022 RP-Steuerberatung</div></div>
    <div><h4>QUICK LINKS</h4><ul><li>Home</li><li>Leistungen</li><li>Über mich</li><li>Impressum</li><li>Kontakt</li></ul></div>
    <div><h4>CONTACT INFORMATION</h4><div class="ci"><i class="ico"></i><div><small>Email:</small><span>office@rp-steuer.example</span></div></div><div class="ci"><i class="ico"></i><div><small>Phone:</small><span>+43 512 000 471</span></div></div><div class="social-row">Social Media: <i></i><i></i><i></i></div></div>
  </footer>
</section>

<!-- HOME 2 -->
<section class="page" style="left:82px;top:728px;height:536px">
  <div class="topbar"><div class="social"><i></i><i></i><i></i></div><div class="contact"><span>Email: office@rp-steuer.example</span><span>Phone: <b>+43 512 000 471</b></span></div></div>
  <nav class="nav"><div class="brand"><span class="mark"></span>RP STEUERBERATUNG</div><div class="menu"><span class="on">HOME</span><span>LEISTUNGEN ▾</span><span>ÜBER MICH</span><span>IMPRESSUM</span><span class="btn-k">KONTAKT ›</span></div></nav>
  <div class="hero">
    <div class="photo" role="img" aria-label="Foto: Beratungsgespräch zweier Geschäftsmänner am Laptop, Krypto-Münzen oben links" style="background:linear-gradient(90deg,#f5f6f8 0%,#e9ecf0 45%,#b9bfca 62%,#4a5064 80%,#23283a 100%)"></div>
    <div class="copy low"><h1>WILLKOMMEN BEI<strong>RP-STEUERBERATUNG!</strong></h1><p>Ihrem Spezialisten bei allen steuerlichen Themen rund um Einkünfte &amp; Vermögen aus Krypto-Assets.</p><span class="pill">WEITER ZU UNSEREN LEISTUNGEN <svg viewBox="0 0 10 10"><circle cx="5" cy="5" r="4" fill="none" stroke="#fff"/><path d="M4 3l2 2-2 2" fill="none" stroke="#fff"/></svg></span></div>
    <div class="arrow-nav" style="left:0;background:#b3b7bf">‹</div><div class="arrow-nav" style="right:0">›</div>
  </div>
  <div class="features">
    <div class="feature"><span class="num">01</span><p>Dann mach ich eine Schweizer Holding Gesellschaft- dort zahlt man fast keine Steuern</p></div>
    <div class="feature"><span class="num">02</span><p>Dann melde ich einfach meinen Hauptwohnsitz in Österreich ab</p></div>
    <div class="feature"><span class="num">03</span><p>Dann lass ich meine Kryptos auf einer Börse in Singapur, dort ist das steuerfrei</p></div>
  </div>
  <footer class="footer">
    <div><div class="brand"><span class="mark"></span>RP STEUERBERATUNG</div>Ihrem Spezialisten bei allen steuerlichen Themen rund um Einkünfte &amp; Vermögen aus Krypto-Assets.<div class="copy">Copyright © 2022 RP-Steuerberatung</div></div>
    <div><h4>QUICK LINKS</h4><ul><li>Home</li><li>Leistungen</li><li>Über mich</li><li>Impressum</li><li>Kontakt</li></ul></div>
    <div><h4>CONTACT INFORMATION</h4><div class="ci"><i class="ico"></i><div><small>Email:</small><span>office@rp-steuer.example</span></div></div><div class="ci"><i class="ico"></i><div><small>Phone:</small><span>+43 512 000 471</span></div></div><div class="social-row">Social Media: <i></i><i></i><i></i></div></div>
  </footer>
</section>

<!-- ABOUT -->
<section class="page" style="left:82px;top:1345px;height:892px">
  <div class="topbar"><div class="social"><i></i><i></i><i></i></div><div class="contact"><span>Email: office@rp-steuer.example</span><span>Phone: <b>+43 512 000 471</b></span></div></div>
  <nav class="nav"><div class="brand"><span class="mark"></span>RP STEUERBERATUNG</div><div class="menu"><span>HOME</span><span>LEISTUNGEN ▾</span><span class="on">ÜBER MICH</span><span>IMPRESSUM</span><span class="btn-k">KONTAKT ›</span></div></nav>
  <div class="banner"><div class="photo" role="img" aria-label="Foto: Hand zieht Krypto-Münzen aus einer braunen Geldbörse"></div><h2>ÜBER MICH</h2></div>
  <div class="intro">
    <div class="ring"><div class="photo" role="img" aria-label="Porträtfoto des Steuerberaters im grauen Anzug mit Smartphone"></div></div>
    <div class="namecard"><b>Mag. Peter Rainer</b><small>Professional Tax Advisor</small></div>
    <div class="about-text">
      <p>Mag. Peter Rainer Ich blicke auf eine sehr umfassende Ausbildung und langjährige Berufserfahrung in der IT Branche zurück. Nach Abschluss des Wirtschaftsstudiums habe ich den klassischen Weg der Steuerberaterausbildung absolviert und bin in diesem Bereich seit über 13 Jahren beratend tätig.</p>
      <p>Durch die Kombination meines umfassenden Wissens in der IT und der Wirtschaft habe ich schon immer gerne Unternehmen mit besonderes technischen oder digitalen Geschäftsmodellen beraten. Seit mehreren Jahren bin ich privat an der Blockchaintechnologie und dem Krypto-Universum interessiert und bereits seit dem Jahre 2017 ist dieses Thema auch Teil meiner fixen Beratungsfelder in der Steuerberatung.</p>
    </div>
  </div>
  <div class="timeline">
    <div class="tl-cols">
      <div><h5>Ausbildung</h5>
        <div class="row"><span class="yr">2002</span><span>HTL - Matura mit Schwerpunkt IT und Betrieblicher Organisation</span></div>
        <div class="row"><span class="yr g">2009</span><span>Studium BWL mit Schwerpunkten Banking &amp; Finance sowie Kapitalmärkte</span></div>
        <div class="row"><span class="yr">2012</span><span>Buchhalter &amp; Bilanzbuchhalterprüfung</span></div>
        <div class="row"><span class="yr g">2013</span><span>Angelobung zum Steuerberater</span></div>
      </div>
      <div><h5>Beruflicher Werdegang</h5>
        <div class="row"><span class="yr">2003-09</span><span>Selbständig tätig im IT Sektor</span></div>
        <div class="row"><span class="yr g">2009</span><span>Beratend tätig in der Steuerberatung / Wirtschaftsprüfung in verschiedenen Kanzleien. Zuletzt in leitender Funktion bei Alpen Treuhand Tirol</span></div>
        <div class="row"><span class="yr">2022</span><span>Gründung der eigenen Kanzlei RP-Steuerberatung mit Fokus Krypto-Beratung.</span></div>
      </div>
    </div>
    <div class="tl-btn"><span class="pill">GO TO MY PRONET PROFILE &nbsp;|&nbsp; <svg viewBox="0 0 10 10"><rect x="2" y="2" width="6" height="6" fill="#fff"/></svg></span></div>
  </div>
  <footer class="footer">
    <div><div class="brand"><span class="mark"></span>RP STEUERBERATUNG</div>Ihrem Spezialisten bei allen steuerlichen Themen rund um Einkünfte &amp; Vermögen aus Krypto-Assets.<div class="copy">Copyright © 2022 RP-Steuerberatung</div></div>
    <div><h4>QUICK LINKS</h4><ul><li>Home</li><li>Leistungen</li><li>Über mich</li><li>Impressum</li><li>Kontakt</li></ul></div>
    <div><h4>CONTACT INFORMATION</h4><div class="ci"><i class="ico"></i><div><small>Email:</small><span>office@rp-steuer.example</span></div></div><div class="ci"><i class="ico"></i><div><small>Phone:</small><span>+43 512 000 471</span></div></div><div class="social-row">Social Media: <i></i><i></i><i></i></div></div>
  </footer>
</section>

<!-- SERVICE -->
<section class="page" style="left:634px;top:110px;height:792px">
  <div class="topbar"><div class="social"><i></i><i></i><i></i></div><div class="contact"><span>Email: office@rp-steuer.example</span><span>Phone: <b>+43 512 000 471</b></span></div></div>
  <nav class="nav"><div class="brand"><span class="mark"></span>RP STEUERBERATUNG</div><div class="menu"><span>HOME</span><span class="on">LEISTUNGEN</span><span>ÜBER MICH</span><span>IMPRESSUM</span><span class="btn-k">KONTAKT ›</span></div></nav>
  <div class="banner"><div class="photo" role="img" aria-label="Foto: Hand hält eine Geldbörse mit Krypto-Münzen"></div><h2>LEISTUNGEN</h2></div>
  <div class="section" style="height:472px">
    <p class="lead">Ich biete in meiner Kanzlei ausschließlich Spezialberatung rund um die komplexen und vielseitigen Themen im Krypto-Bereich sowie deren Besteuerung, bzw. der Besteuerung und steuerlichen Optimierung von anderen passiven Einkommensmodellen an:</p>
    <ul class="checks">
      <li><svg viewBox="0 0 10 10"><circle cx="5" cy="5" r="5" fill="#13213f"/><path d="M2.8 5.2l1.5 1.5 3-3" fill="none" stroke="#fff" stroke-width="1.2"/></svg><span>Steueroptimales Besitzen von KryptoAssets auf in- und ausländischen Börsen</span></li>
      <li><svg viewBox="0 0 10 10"><circle cx="5" cy="5" r="5" fill="#13213f"/><path d="M2.8 5.2l1.5 1.5 3-3" fill="none" stroke="#fff" stroke-width="1.2"/></svg><span>Hilfestellung bei der Dokumentation der Einkünfte (Verwendung von Tax-Tools und Aufbereitung der Daten, etc.)</span></li>
      <li><svg viewBox="0 0 10 10"><circle cx="5" cy="5" r="5" fill="#13213f"/><path d="M2.8 5.2l1.5 1.5 3-3" fill="none" stroke="#fff" stroke-width="1.2"/></svg><span>Finanzstrafrechtliche Offenlegung und Aufarbeitung bei Einkünften die nicht ordnungsgemäß erklärt wurden</span></li>
      <li><svg viewBox="0 0 10 10"><circle cx="5" cy="5" r="5" fill="#13213f"/><path d="M2.8 5.2l1.5 1.5 3-3" fill="none" stroke="#fff" stroke-width="1.2"/></svg><span>Beratung rund um das Thema Wegzug, Wohnsitzverlegung und in-/ausländische Gesellschaften</span></li>
      <li><svg viewBox="0 0 10 10"><circle cx="5" cy="5" r="5" fill="#13213f"/><path d="M2.8 5.2l1.5 1.5 3-3" fill="none" stroke="#fff" stroke-width="1.2"/></svg><span>Hilfe bei der korrekten Erklärung der Crypto-Einkünfte und Erstellung der Steuererklärungen</span></li>
      <li><svg viewBox="0 0 10 10"><circle cx="5" cy="5" r="5" fill="#13213f"/><path d="M2.8 5.2l1.5 1.5 3-3" fill="none" stroke="#fff" stroke-width="1.2"/></svg><span>Beratung bei der Unterscheidung und Besteuerung der diversen Einkunftsmöglichkeiten (Trading, Staking, Lending, Mining, Nodes, NFTs, , etc.)</span></li>
    </ul>
    <div class="framed" style="left:268px;top:91px;width:176px;height:244px"><div class="photo" role="img" aria-label="Foto: Hand tippt auf ein leuchtendes Börsendiagramm" style="left:2px;top:2px;width:168px;height:236px;background:linear-gradient(160deg,#1b2a4c 0%,#2d5a8a 50%,#0f2240 100%)"></div></div>
    <p class="lead" style="position:absolute;left:38px;right:38px;top:364px;padding:0 20px">Werden neben der Spezialberatung auch noch klassische Services wie Buchhaltung, Lohnverrechnung etc. benötigt, kann dies gerne über Partner-Kanzleien von mir organisiert werden.</p>
    <div class="center" style="position:absolute;left:0;right:0;top:416px"><span class="pill">NEHMEN SIE GERNE KONTAKT MIT MIR AUF! <svg viewBox="0 0 10 10"><circle cx="5" cy="5" r="4" fill="none" stroke="#fff"/><path d="M4 3l2 2-2 2" fill="none" stroke="#fff"/></svg></span></div>
  </div>
  <footer class="footer">
    <div><div class="brand"><span class="mark"></span>RP STEUERBERATUNG</div>Ihrem Spezialisten bei allen steuerlichen Themen rund um Einkünfte &amp; Vermögen aus Krypto-Assets.<div class="copy">Copyright © 2022 RP-Steuerberatung</div></div>
    <div><h4>QUICK LINKS</h4><ul><li>Home</li><li>Leistungen</li><li>Über mich</li><li>Impressum</li><li>Kontakt</li></ul></div>
    <div><h4>CONTACT INFORMATION</h4><div class="ci"><i class="ico"></i><div><small>Email:</small><span>office@rp-steuer.example</span></div></div><div class="ci"><i class="ico"></i><div><small>Phone:</small><span>+43 512 000 471</span></div></div><div class="social-row">Social Media: <i></i><i></i><i></i></div></div>
  </footer>
</section>

<!-- COLLEAGUES -->
<section class="page" style="left:634px;top:983px;height:711px">
  <div class="topbar"><div class="social"><i></i><i></i><i></i></div><div class="contact"><span>Email: office@rp-steuer.example</span><span>Phone: <b>+43 512 000 471</b></span></div></div>
  <nav class="nav"><div class="brand"><span class="mark"></span>RP STEUERBERATUNG</div><div class="menu"><span>HOME</span><span class="on">LEISTUNGEN ▾</span><span>ÜBER MICH</span><span>IMPRESSUM</span><span class="btn-k">KONTAKT ›</span></div></nav>
  <div class="banner"><div class="photo" role="img" aria-label="Foto: Team legt Hände über einem Holztisch zusammen" style="background:linear-gradient(100deg,#1a2744 0%,#3a3f4d 45%,#6a4a32 75%,#3b2c22 100%)"></div><h2>KOLLEGENDIENST</h2></div>
  <div class="section" style="height:392px">
    <p class="q">Ihr Fokus liegt in der traditionellen Steuerberatung und Sie haben keine Zeit sich das hochkomplexe Spezialthema Kryptowährungen etc. einzuarbeiten?</p>
    <p class="lead" style="padding:0 45px">Um Ihre Klienten dennoch weiterhin vollumfänglich beraten zu können, biete ich Ihnen gerne mein Know-How und die gesamte Leistungspalette an um Ihre Kunden ganz nach Ihrem Wunsch entweder direkt oder diskret im Hintergrund bei sämtlichen Themen rund um Krypto mit steuerlicher Expertise dazu zu unterstützen.</p>
    <svg style="position:absolute;left:230px;top:130px" width="24" height="22" viewBox="0 0 24 22"><path d="M20 3C12 3 7 8 6 17" fill="none" stroke="#333" stroke-width="1"/><path d="M3 13l3 5 4-4" fill="none" stroke="#333" stroke-width="1"/></svg>
    <div class="framed" style="left:52px;top:166px;width:386px;height:148px;border-top:0;border-left:0"></div>
    <div class="photo" role="img" aria-label="Foto: vier Kolleginnen und Kollegen im Business-Outfit besprechen Unterlagen" style="position:absolute;left:52px;top:166px;width:382px;height:144px;border-radius:8px;background:linear-gradient(90deg,#3b4150 0%,#8f949c 35%,#c9ccd1 55%,#7a7f88 80%,#2d323d 100%)"></div>
    <div class="center" style="position:absolute;left:0;right:0;top:337px"><span class="pill">NEHMEN SIE GERNE KONTAKT MIT MIR AUF! <svg viewBox="0 0 10 10"><circle cx="5" cy="5" r="4" fill="none" stroke="#fff"/><path d="M4 3l2 2-2 2" fill="none" stroke="#fff"/></svg></span></div>
  </div>
  <footer class="footer">
    <div><div class="brand"><span class="mark"></span>RP STEUERBERATUNG</div>Ihrem Spezialisten bei allen steuerlichen Themen rund um Einkünfte &amp; Vermögen aus Krypto-Assets.<div class="copy">Copyright © 2022 RP-Steuerberatung</div></div>
    <div><h4>QUICK LINKS</h4><ul><li>Home</li><li>Leistungen</li><li>Über mich</li><li>Impressum</li><li>Kontakt</li></ul></div>
    <div><h4>CONTACT INFORMATION</h4><div class="ci"><i class="ico"></i><div><small>Email:</small><span>office@rp-steuer.example</span></div></div><div class="ci"><i class="ico"></i><div><small>Phone:</small><span>+43 512 000 471</span></div></div><div class="social-row">Social Media: <i></i><i></i><i></i></div></div>
  </footer>
</section>

</body>
</html>
```